Corwell's Finest magazine ad

This is a full page ad in a magazine announcing that I won The Finest Of Corwell Valley Realtor for 2023. The dimensions for the full page ad are 7.125" x 9.75"
I would like it to say "Thank You Harford County for voting me Corwell's Finest Realtor for 2022 & 2023!"

I am honored that the residents of this county have recognized my integrity, values, willingness to go above and beyond, to save my clients tons of money and stress, and to constantly pour back into this community.

If you are ever thinking about buying or selling a house, please don't hesitate to reach out, I am available 24/7 by text or phone call to save you money and provide the best top notch service:

Marcus Pellow
call/text 410-555-0147

Small at the bottom:
www.SummitKeyHomes.example
2870 W Alderbrook Ln, Bel Air, MD 21014
833-555-0192

I am attaching my logo, the Corwell's Finest 2023 logo, my picture, and last years ad (I'm hoping to make this years ad different and better)

```html
<!DOCTYPE html>
<html lang="en">
<head>
<meta charset="utf-8">
<title>Corwell's Finest Realtor – Thank You Ad</title>
<link href="https://fonts.googleapis.com/css2?family=Bebas+Neue&family=Great+Vibes&family=Allura&family=Urbanist:wght@400;600;700;800&display=swap" rel="stylesheet">
<style>
  :root{
    --backdrop:#9d9c9d;
    --paper:#ffffff;
    --blue-deep:#243f95;
    --blue-bright:#1676c0;
    --navy:#1d2b52;
    --red:#bd1f2e;
    --script-grey:#cfd0d4;
    --gold:#f4e400;
    --ink:#1f1f22;
    --badge:#231f20;
  }
  *{margin:0;padding:0;box-sizing:border-box}
  html,body{width:956px;height:1200px;overflow:hidden;background:var(--backdrop)}
  .ad{position:absolute;left:110px;top:95px;width:737px;height:1009px;background:var(--paper);overflow:hidden;font-family:"Urbanist",sans-serif}
  .hero{position:absolute;left:0;top:0;width:737px;height:551px;background:linear-gradient(120deg,var(--blue-deep) 0%,#1f5aa8 55%,var(--blue-bright) 100%)}
  .portrait{position:absolute;left:380px;top:40px;width:357px;height:511px;background:linear-gradient(180deg,#3c4a6b 0%,#2a3858 40%,#1f2b47 100%);border-radius:150px 150px 0 0}
  .thanks{position:absolute;left:44px;top:18px;font-family:"Great Vibes",cursive;font-size:100px;line-height:1;color:var(--script-grey);z-index:2;white-space:nowrap}
  .voters{position:absolute;left:48px;top:133px;font-size:33px;line-height:32px;color:#fff;font-weight:400;z-index:2}
  .headline{position:absolute;left:46px;top:206px;font-family:"Bebas Neue",sans-serif;font-size:86px;line-height:78px;color:#fff;font-weight:400;z-index:2;white-space:nowrap}
  .message{position:absolute;left:40px;top:578px;width:360px;font-size:17px;line-height:20.2px;color:var(--ink)}
  .message .lead{font-weight:700;margin-bottom:20px}
  .message .invite{font-weight:400}
  .award-badge{position:absolute;left:490px;top:524px;width:143px;height:126px}
  .brand{position:absolute;left:470px;top:716px;width:178px;display:flex;align-items:center;justify-content:center;gap:8px;color:var(--navy);font-weight:700;font-size:19px;letter-spacing:.5px;white-space:nowrap}
  .brand .dot{width:14px;height:14px;border-radius:50%;background:var(--navy)}
  .contact-band{position:absolute;left:0;top:817px;width:737px;height:107px}
  .call{position:absolute;left:0;top:834px;width:382px;text-align:center;color:#fff;font-weight:800}
  .call .label{font-size:26px;line-height:30px}
  .call .number{font-size:47px;line-height:52px;letter-spacing:.5px}
  .signature{position:absolute;left:397px;top:836px;width:330px;text-align:center;font-family:"Allura",cursive;font-size:60px;line-height:72px;color:var(--gold);white-space:nowrap}
  .footer{position:absolute;left:0;top:938px;width:737px;text-align:center;color:var(--ink);font-size:14.5px;line-height:17px}
  .footer .gap{display:inline-block;width:20px}
</style>
</head>
<body>
<main class="ad">
  <section class="hero">
    <div class="portrait" role="img" aria-label="Portrait photo of the realtor in a navy suit jacket and striped shirt"></div>
    <div class="thanks">Thank you</div>
    <p class="voters">Harford County<br>for voting me</p>
    <h1 class="headline">CORWELL'S<br>FINEST REALTOR<br>FOR 2022 &amp;<br>2023!</h1>
  </section>

  <svg class="award-badge" viewBox="0 0 143 128" aria-hidden="true">
    <polygon points="71.5,0 100,8 124,24 140,50 140,80 124,104 100,120 71.5,128 43,120 19,104 3,80 3,50 19,24 43,8" fill="var(--badge)"/>
  </svg>

  <div class="message">
    <p class="lead">I am honored that the residents of this county have recognized my integrity, values, willingness to go above and beyond, to save my clients tons of money and stress, and to constantly pour back into this community.</p>
    <p class="invite">If you are ever thinking about buying or selling a house, please don't hesitate to reach out, I am available 24/7 by text or phone call to save you money and provide the best top notch service:</p>
  </div>

  <div class="brand"><span class="dot"></span>SUMMIT KEY HOMES</div>

  <svg class="contact-band" viewBox="0 0 737 107" preserveAspectRatio="none" aria-hidden="true">
    <defs>
      <linearGradient id="bandBlue" x1="0" x2="1" y1="0" y2="0">
        <stop offset="0" stop-color="#243f95"/>
        <stop offset="1" stop-color="#1676c0"/>
      </linearGradient>
    </defs>
    <rect x="0" y="0" width="737" height="107" fill="url(#bandBlue)"/>
    <polygon points="0,0 396,0 351,107 0,107" fill="var(--red)"/>
    <polygon points="396,0 406,0 363,107 351,107" fill="#ffffff"/>
  </svg>

  <div class="call">
    <div class="label">call/text</div>
    <div class="number">410-555-0147</div>
  </div>

  <div class="signature">Marcus Pellow</div>

  <footer class="footer">
    <div>www.SummitKeyHomes.example</div>
    <div>2870 W Alderbrook Ln, Bel Air, MD 21014<span class="gap"></span>833-555-0192</div>
  </footer>
</main>
</body>
</html>
```